Visitenkarten-Design für virtuelle Jobmesse & Jobbörse für Soldaten
Zielgruppe
Die KLO GmbH ist ein Unternehmen das zwei Hauptprodukte betreibt! Zum einen Jobbörse für Soldaten unter www.wachwechselpunkt.de und zum anderen eine virtuelle Jobmesse für Soldaten unter www.marvento.de , die wir zweimal im Jahr veranstalten.
Aufgabenstellung
Wir haben ja die beiden Produkte Wachwechselpunkt.de und die Marvento, für die bereits jeweils ein separtes Logo besteht! Diese finden Sie im Anhang! Beide werden doch jedoch von einem Unternehmen, der KLO GmbH betrieben! Aktuell nutzen wir eine Visitenkarte mit dem Logo von KLO und eine mit dem Logo der MARVENTO. Gerade im Hinblick darauf, dass wir zukünftig auch weiter Plattformen in unser Portfolio aufnehmen, möchte ich hier unsere V-Karten flexibler gestalten!
Ziel soll es also sein, eine Visitenkarte zu gestalten, auf dem klar wird, dass der Mitarbeiter von der KLO GmbH kommt, die KLO GmbH aber unterschiedliche Produkte betreibt.
Im Anhang finden Sie:
1. Das Logo von KLO
2. Das Logo von Marvento
3. Die aktuelle V-Karte von KLO
4. Die aktuelle V-Karte von MARVENTO
Vielleicht ein kleiner Anreiz: Aktuell nutzen wir auch zwei getrennte Geschäftspapiere. Das von www.wachwechselpunkt.de lade ich einmal hoch! Der Designer, der auch die Visitenkarte erstellt, erhällt im Anschluss den 1:1 Auftrag in Höhe von 200 Euro für die Erstellung des Geschäftspapiers! Wenn Sie jetzt schon einen Vorschlag für das Geschäftspapier einreichen, erhöht das natürlich Ihre Chancen, wobei ich verspreche, dass wir im Falle eine Annahme das 1:1 im Anschluß dennoch starten werden!

```html
<!DOCTYPE html>
<html lang="de">
<head>
<meta charset="utf-8">
<title>Visitenkarten – KLO GmbH</title>
<link rel="stylesheet" href="https://fonts.googleapis.com/css2?family=Arimo:wght@400;700&display=swap">
<style>
  :root {
    --blue: #1f497d;
    --green: #3e5a2d;
    --ink: #444444;
    --frame: #555555;
    --paper: #ffffff;
  }
  * { box-sizing: border-box; margin: 0; padding: 0; }
  html, body {
    width: 848px; height: 1200px; overflow: hidden;
    background: var(--paper);
    font-family: "Arimo", Arial, sans-serif;
  }
  .sheet { position: relative; width: 848px; height: 1200px; }
  .card {
    position: absolute;
    width: 342px; height: 221px;
    border: 1px solid var(--frame);
    background: var(--paper);
    overflow: hidden;
    --brand: var(--blue);
  }
  .card--marvento { --brand: var(--green); }
  .card--r1 { top: 189px; }
  .card--r2 { top: 440px; }
  .card--c1 { left: 72px; }
  .card--c2 { left: 444px; }

  .card__arc { position: absolute; left: 0; top: 0; width: 342px; height: 221px; }
  .card__arc path { fill: var(--brand); }

  .person { position: absolute; left: 16px; top: 98px; color: #fff; }
  .person__name { font-size: 13.6px; font-weight: 700; letter-spacing: 0.2px; line-height: 15px; }
  .person__role { font-size: 11px; line-height: 14px; }

  .contact { position: absolute; left: 162px; top: 98px; color: var(--ink); }
  .contact__brand { font-size: 13.6px; font-weight: 700; line-height: 15px; color: var(--brand); letter-spacing: 0.1px; }
  .contact__owner { font-size: 11px; line-height: 14px; color: var(--brand); margin-bottom: 4px; }
  .contact__address { font-size: 9.2px; line-height: 12px; margin-bottom: 4px; }
  .contact__line { font-size: 9.2px; line-height: 13px; white-space: nowrap; }
  .contact__line b { font-weight: 700; }

  .brandmark {
    position: absolute; top: 26px; right: 18px;
    display: flex; align-items: center; gap: 5px;
    color: var(--brand); font-weight: 700;
  }
  .brandmark--wachwechselpunkt { font-size: 10px; top: 32px; right: 20px; }
  .brandmark--marvento { font-size: 15px; top: 30px; right: 14px; letter-spacing: 0.5px; }
  .brandmark__dot { width: 12px; height: 12px; border-radius: 50%; background: var(--brand); }
</style>
</head>
<body>
<div class="sheet">

  <section class="card card--r1 card--c1">
    <svg class="card__arc" viewBox="0 0 342 221" aria-hidden="true"><path d="M0 0 H110 A165 165 0 0 1 98.5 221 H0 Z"/></svg>
    <div class="brandmark brandmark--wachwechselpunkt">Wachwechselpunkt</div>
    <div class="person"><p class="person__name">Tobias Werner</p><p class="person__role">Leiter Vertrieb</p></div>
    <div class="contact">
      <p class="contact__brand">Wachwechselpunkt.de</p>
      <p class="contact__owner">eine Marke der KLO GmbH</p>
      <p class="contact__address">Lindenallee 12 · 86650 Altdorf</p>
      <p class="contact__line"><b>T:</b>&nbsp; 0 81 47 / 52 36 09 2</p>
      <p class="contact__line"><b>E:</b> tobias.werner@wachwechselpunkt.de</p>
      <p class="contact__line"><b>H:</b> www.wachwechselpunkt.de</p>
    </div>
  </section>

  <section class="card card--marvento card--r1 card--c2">
    <svg class="card__arc" viewBox="0 0 342 221" aria-hidden="true"><path d="M0 0 H110 A165 165 0 0 1 98.5 221 H0 Z"/></svg>
    <div class="brandmark brandmark--marvento">MARVENTO<span class="brandmark__dot"></span></div>
    <div class="person"><p class="person__name">Tobias Werner</p><p class="person__role">Leiter Vertrieb</p></div>
    <div class="contact">
      <p class="contact__brand">Marvento.de</p>
      <p class="contact__owner">eine Marke der KLO GmbH</p>
      <p class="contact__address">Lindenallee 12 · 86650 Altdorf</p>
      <p class="contact__line"><b>T:</b>&nbsp; 0 81 47 / 52 36 09 2</p>
      <p class="contact__line"><b>E:</b> tobias.werner@marvento.de</p>
      <p class="contact__line"><b>H:</b> www.marvento.de</p>
    </div>
  </section>

  <section class="card card--r2 card--c1">
    <svg class="card__arc" viewBox="0 0 342 221" aria-hidden="true"><path d="M0 0 H110 A165 165 0 0 1 98.5 221 H0 Z"/></svg>
    <div class="brandmark brandmark--wachwechselpunkt">Wachwechselpunkt</div>
    <div class="person"><p class="person__name">Tobias Werner</p><p class="person__role">Leiter Vertrieb</p></div>
    <div class="contact">
      <p class="contact__brand">Wachwechselpunkt.de</p>
      <p class="contact__owner">eine Marke der KLO GmbH</p>
      <p class="contact__address">Lindenallee 12 · 86650 Altdorf</p>
      <p class="contact__line"><b>T:</b>&nbsp; 0 81 47 / 52 36 09 2</p>
      <p class="contact__line"><b>E:</b> tobias.werner@wachwechselpunkt.de</p>
      <p class="contact__line"><b>H:</b> www.wachwechselpunkt.de</p>
    </div>
  </section>

  <section class="card card--marvento card--r2 card--c2">
    <svg class="card__arc" viewBox="0 0 342 221" aria-hidden="true"><path d="M0 0 H110 A165 165 0 0 1 98.5 221 H0 Z"/></svg>
    <div class="brandmark brandmark--marvento">MARVENTO<span class="brandmark__dot"></span></div>
    <div class="person"><p class="person__name">Tobias Werner</p><p class="person__role">Leiter Vertrieb</p></div>
    <div class="contact">
      <p class="contact__brand">Marvento.de</p>
      <p class="contact__owner">eine Marke der KLO GmbH</p>
      <p class="contact__address">Lindenallee 12 · 86650 Altdorf</p>
      <p class="contact__line"><b>T:</b>&nbsp; 0 81 47 / 52 36 09 2</p>
      <p class="contact__line"><b>E:</b> tobias.werner@marvento.de</p>
      <p class="contact__line"><b>H:</b> www.marvento.de</p>
    </div>
  </section>

</div>
</body>
</html>
```